Design a Travel and Tourism website

We would like a freelancer to design a website that is essentially easy to use and navigate database providing local information for Travelers about destination countries.

We proposed website would discuss different rates, fees, visa requirement, resort locations, cheap flights, etc. This website should be elegant and modern. Our business name is mirdalon.
Some reference websites are plendavix.ca, gosthandiverquo.com,
There should be a forum in the website where travell\ers discuss about their first hand tranvel experience to such destinations.

```html
<!DOCTYPE html>
<html lang="en">
<head>
<meta charset="utf-8">
<title>mirdalon — Find the perfect deals</title>
<link href="https://fonts.googleapis.com/css2?family=Open+Sans:ital,wght@0,400;0,600;0,700;0,800;1,400&family=Dancing+Script:wght@400;600&display=swap" rel="stylesheet">
<style>
:root{
  --accent:#93b597;
  --accent-soft:#b7c9a5;
  --ink:#222;
  --muted:#555;
  --page:#ffffff;
  --band:#f1f1f1;
  --panel:rgba(45,48,45,.82);
  --footer-text:#c9cbc9;
  --caption:rgba(30,30,30,.55);
}
*{box-sizing:border-box;margin:0;padding:0}
html,body{width:1200px;height:3371px;overflow:hidden;background:var(--page);font-family:"Open Sans",Arial,sans-serif;color:var(--ink)}
.page{position:relative;width:1200px;height:3371px;overflow:hidden}

/* hero */
.hero{position:absolute;left:0;top:0;width:1200px;height:872px}
.hero-bg{position:absolute;inset:0}
.nav{position:absolute;top:0;left:0;width:1200px;height:90px}
.menu-icon{position:absolute;left:58px;top:32px;width:26px;height:20px}
.menu-icon span{display:block;height:3px;background:#fff;margin-bottom:5px;border-radius:2px}
.nav-link{position:absolute;top:34px;font-family:"Dancing Script",cursive;color:#fff;font-size:17px}
.logo{position:absolute;left:0;width:1200px;top:16px;text-align:center;font-family:"Open Sans",sans-serif;font-weight:400;font-size:44px;color:#fff;letter-spacing:1px}
.headline{position:absolute;top:242px;width:1200px;text-align:center;color:#fff;font-weight:600;font-size:40px;line-height:54px;letter-spacing:1px}
.headline .hl{color:var(--accent-soft)}

.search{position:absolute;left:243px;top:402px;width:714px;height:286px;background:var(--panel)}
.tabs{display:flex;height:38px}
.tab{flex:1;color:#fff;font-size:13px;font-weight:700;text-align:center;line-height:38px;background:rgba(20,22,20,.6)}
.tab.active{background:var(--accent)}
.field-label{position:absolute;color:#fff;font-size:12px;line-height:14px;text-align:right;width:110px;white-space:nowrap}
.field{position:absolute;height:26px;background:#fff;border-radius:2px;font-size:10px;line-height:14px;color:#aaa;padding:6px 10px}
.select{position:absolute;width:46px;height:26px;background:#fff;border-radius:2px}
.select::after{content:"";position:absolute;right:7px;top:10px;border:5px solid transparent;border-top-color:#444}
.search-btn{position:absolute;left:476px;top:207px;width:190px;height:48px;background:var(--accent);color:#fff;font-size:15px;font-weight:600;display:flex;align-items:center;justify-content:center;gap:12px;letter-spacing:1px}

/* sections */
.deco-mark{position:absolute;left:300px;top:960px;width:600px;height:1120px;border-radius:50%;background:radial-gradient(circle,rgba(0,0,0,.035),rgba(0,0,0,.015) 70%,transparent 72%)}
.kicker{position:absolute;width:1200px;text-align:center;font-family:"Dancing Script",cursive;font-size:21px;color:#333}
.section-title{position:absolute;width:1200px;text-align:center;font-weight:800;font-size:33px;letter-spacing:1px;color:var(--ink)}
.carousel{position:absolute;left:0;width:1200px;height:319px;background:var(--band);border-radius:18px}
.arrow{position:absolute;top:136px;width:22px;height:40px}
.card{position:absolute;top:0;width:355px;height:319px;overflow:hidden}
.card .photo{position:absolute;inset:0}
.card .caption{position:absolute;left:0;bottom:0;width:100%;height:86px;background:var(--caption);padding:10px 18px;color:#fff}
.card .city{font-size:33px;font-weight:600;line-height:40px}
.card .price{font-size:17px;font-weight:600}
.card .expand{position:absolute;right:14px;bottom:12px;width:16px;height:16px}

.post{position:absolute;left:148px;width:892px;height:234px;background:#fff;box-shadow:0 1px 6px rgba(0,0,0,.28)}
.post .photo{position:absolute;left:0;top:0;width:276px;height:100%}
.post-body{position:absolute;left:316px;top:22px;width:520px}
.post-title{font-size:29px;line-height:38px;color:var(--accent);font-weight:400;letter-spacing:.5px}
.post-author{font-size:12px;font-style:italic;color:#666;margin-top:0}
.post-author span{text-decoration:underline}
.post-text{font-size:13px;line-height:20px;color:#333;margin-top:4px}
.read-more{position:absolute;right:80px;bottom:18px;font-size:12px;color:var(--accent);letter-spacing:.5px}
.forum-btn{position:absolute;left:463px;top:2901px;width:274px;height:70px;border:2px solid #444;font-size:16px;text-align:center;line-height:66px;letter-spacing:.5px}

/* footer */
.footer{position:absolute;left:0;top:3047px;width:1200px;height:324px;background:linear-gradient(180deg,#2f3331,#232624);color:var(--footer-text)}
.f-col{position:absolute;top:45px}
.f-col h4{font-size:14px;font-weight:700;letter-spacing:1.5px;color:#ddd;margin-bottom:30px}
.f-col a{display:block;font-size:14px;color:var(--footer-text);text-decoration:none;line-height:36px;letter-spacing:.5px}
.copyright{position:absolute;left:70px;top:286px;font-size:11px;color:#aaa}
.copyright span{text-decoration:underline}
.social{position:absolute;right:70px;top:282px;display:flex;gap:6px}
.social i{display:block;width:20px;height:20px;border-radius:50%;background:#8b8e8c}
</style>
</head>
<body>
<div class="page">

  <header class="hero">
    <svg class="hero-bg" width="1200" height="872" viewBox="0 0 1200 872" role="img" aria-label="Photo of a hiker with a backpack standing on a misty mountain ridge">
      <defs>
        <linearGradient id="heroFill" x1="0" y1="0" x2="0" y2="1">
          <stop offset="0" stop-color="#8a978f"/>
          <stop offset=".5" stop-color="#75836f"/>
          <stop offset="1" stop-color="#4e5a4c"/>
        </linearGradient>
      </defs>
      <path d="M0 0H1200V764Q600 980 0 764Z" fill="url(#heroFill)"/>
    </svg>
    <nav class="nav">
      <div class="menu-icon"><span></span><span></span><span></span></div>
      <span class="nav-link" style="left:180px">Home</span>
      <span class="nav-link" style="left:266px">Flights</span>
      <span class="nav-link" style="left:352px">Hotels</span>
      <span class="nav-link" style="left:438px">Cars</span>
      <div class="logo">mirdalon</div>
      <span class="nav-link" style="left:734px">Travel Insurance</span>
      <span class="nav-link" style="left:878px">Travel Costs</span>
      <span class="nav-link" style="left:998px">Forums</span>
    </nav>
    <h1 class="headline">FIND THE PERFECT <span class="hl">DEALS</span> FOR<br>YOUR PERFECT <span class="hl">HOLIDAYS</span></h1>

    <form class="search">
      <div class="tabs">
        <div class="tab active">FLIGHTS</div><div class="tab">HOTELS</div><div class="tab">CARS</div><div class="tab">INSURANCE</div><div class="tab">EXTRAS</div>
      </div>
      <label class="field-label" style="left:0;top:79px">Depart from:</label>
      <div class="field" style="left:125px;top:73px;width:212px">City or airport</div>
      <label class="field-label" style="left:0;top:128px">Depart to:</label>
      <div class="field" style="left:125px;top:122px;width:212px">City or airport</div>
      <label class="field-label" style="left:330px;top:79px">Depart date:</label>
      <div class="field" style="left:454px;top:73px;width:212px">DD/MM/YYYY</div>
      <label class="field-label" style="left:330px;top:128px">Return date:</label>
      <div class="field" style="left:454px;top:122px;width:212px">DD/MM/YYYY</div>
      <label class="field-label" style="left:0;top:175px">Adults:</label>
      <div class="select" style="left:124px;top:169px"></div>
      <label class="field-label" style="left:0;top:222px">Children:</label>
      <div class="select" style="left:124px;top:216px"></div>
      <div class="search-btn">
        <svg width="20" height="20" viewBox="0 0 20 20"><circle cx="8" cy="8" r="6" fill="none" stroke="#fff" stroke-width="3"/><path d="M12.5 12.5L18 18" stroke="#fff" stroke-width="3" stroke-linecap="round"/></svg>
        SEARCH
      </div>
    </form>
  </header>

  <div class="deco-mark" role="img" aria-label="Faint travel stamp illustration in the background"></div>

  <section>
    <p class="kicker" style="top:946px">everybody loves deals</p>
    <h2 class="section-title" style="top:970px">HOTTEST DEALS</h2>
    <div class="carousel" style="top:1067px">
      <svg class="arrow" style="left:12px" viewBox="0 0 22 40"><path d="M18 4L5 20L18 36" fill="none" stroke="var(--accent)" stroke-width="5"/></svg>
      <article class="card" style="left:61px">
        <div class="photo" role="img" aria-label="Photo of a turquoise bay and white beach" style="background:linear-gradient(160deg,#5b7f72,#2fb6d8 55%,#e9e4da)"></div>
        <div class="caption"><div class="city">Casa Blanca</div><div class="price">From 120$/person</div></div>
        <svg class="expand" viewBox="0 0 16 16"><path d="M1 1h5L1 6zM15 1v5L10 1zM1 15v-5l5 5zM15 15h-5l5-5z" fill="#fff"/></svg>
      </article>
      <article class="card" style="left:427px">
        <div class="photo" role="img" aria-label="Photo of a lit city square market at dusk" style="background:linear-gradient(180deg,#2a4a8a,#8a5a3a 45%,#6a2a22)"></div>
        <div class="caption"><div class="city">Paris</div><div class="price">From 120$/person</div></div>
        <svg class="expand" viewBox="0 0 16 16"><path d="M1 1h5L1 6zM15 1v5L10 1zM1 15v-5l5 5zM15 15h-5l5-5z" fill="#fff"/></svg>
      </article>
      <article class="card" style="left:791px">
        <div class="photo" role="img" aria-label="Photo of an illuminated baroque fountain" style="background:linear-gradient(180deg,#26325a,#8a6a40 40%,#4a3a2a)"></div>
        <div class="caption"><div class="city">Rome</div><div class="price">From 120$/person</div></div>
        <svg class="expand" viewBox="0 0 16 16"><path d="M1 1h5L1 6zM15 1v5L10 1zM1 15v-5l5 5zM15 15h-5l5-5z" fill="#fff"/></svg>
      </article>
      <svg class="arrow" style="right:12px" viewBox="0 0 22 40"><path d="M4 4L17 20L4 36" fill="none" stroke="var(--accent)" stroke-width="5"/></svg>
    </div>
  </section>

  <section>
    <p class="kicker" style="top:1465px">people trust other people</p>
    <h2 class="section-title" style="top:1489px">HOTTEST PLACES</h2>
    <div class="carousel" style="top:1586px">
      <svg class="arrow" style="left:12px" viewBox="0 0 22 40"><path d="M18 4L5 20L18 36" fill="none" stroke="var(--accent)" stroke-width="5"/></svg>
      <article class="card" style="left:61px">
        <div class="photo" role="img" aria-label="Photo of a turquoise bay and white beach" style="background:linear-gradient(160deg,#5b7f72,#2fb6d8 55%,#e9e4da)"></div>
        <div class="caption"><div class="city">Casa Blanca</div><div class="price">From 120$/person</div></div>
        <svg class="expand" viewBox="0 0 16 16"><path d="M1 1h5L1 6zM15 1v5L10 1zM1 15v-5l5 5zM15 15h-5l5-5z" fill="#fff"/></svg>
      </article>
      <article class="card" style="left:427px">
        <div class="photo" role="img" aria-label="Photo of a lit city square market at dusk" style="background:linear-gradient(180deg,#2a4a8a,#8a5a3a 45%,#6a2a22)"></div>
        <div class="caption"><div class="city">Paris</div><div class="price">From 120$/person</div></div>
        <svg class="expand" viewBox="0 0 16 16"><path d="M1 1h5L1 6zM15 1v5L10 1zM1 15v-5l5 5zM15 15h-5l5-5z" fill="#fff"/></svg>
      </article>
      <article class="card" style="left:791px">
        <div class="photo" role="img" aria-label="Photo of an illuminated baroque fountain" style="background:linear-gradient(180deg,#26325a,#8a6a40 40%,#4a3a2a)"></div>
        <div class="caption"><div class="city">Rome</div><div class="price">From 120$/person</div></div>
        <svg class="expand" viewBox="0 0 16 16"><path d="M1 1h5L1 6zM15 1v5L10 1zM1 15v-5l5 5zM15 15h-5l5-5z" fill="#fff"/></svg>
      </article>
      <svg class="arrow" style="right:12px" viewBox="0 0 22 40"><path d="M4 4L17 20L4 36" fill="none" stroke="var(--accent)" stroke-width="5"/></svg>
    </div>
  </section>

  <section>
    <p class="kicker" style="top:1986px">connect with other</p>
    <h2 class="section-title" style="top:2010px">LATEST FORUM POSTS</h2>

    <article class="post" style="top:2108px">
      <div class="photo" role="img" aria-label="Photo of a traveller in front of a red suspension bridge" style="background:linear-gradient(180deg,#7fa6cf,#b0503a 55%,#5a5a52)"></div>
      <div class="post-body">
        <h3 class="post-title">THE BEST TRAVEL IN YEARS</h3>
        <p class="post-author">by <span>Dara Wendt</span></p>
        <p class="post-text">Lorem ipsum dolor sit amet, consectetur adipisicing elit, sed do eiusmod tempor incididunt ut labore et dolore magna aliqua. Ut enim ad minim veniam, quis nostrud exercitation ullamco laboris nisi ut aliquip ex ea commodo consequat. Duis aute irure dolor in reprehenderit in voluptate velit esse cillum dolore eu fugiat nulla pariatur. Excepteur sint occaecat....</p>
      </div>
      <span class="read-more">READ POST ›</span>
    </article>

    <article class="post" style="top:2371px">
      <div class="photo" role="img" aria-label="Photo of a traveller in front of a red suspension bridge" style="background:linear-gradient(180deg,#7fa6cf,#b0503a 55%,#5a5a52)"></div>
      <div class="post-body">
        <h3 class="post-title">THE BEST TRAVEL IN YEARS</h3>
        <p class="post-author">by <span>Dara Wendt</span></p>
        <p class="post-text">Lorem ipsum dolor sit amet, consectetur adipisicing elit, sed do eiusmod tempor incididunt ut labore et dolore magna aliqua. Ut enim ad minim veniam, quis nostrud exercitation ullamco laboris nisi ut aliquip ex ea commodo consequat. Duis aute irure dolor in reprehenderit in voluptate velit esse cillum dolore eu fugiat nulla pariatur. Excepteur sint occaecat....</p>
      </div>
      <span class="read-more">READ POST ›</span>
    </article>

    <article class="post" style="top:2629px">
      <div class="photo" role="img" aria-label="Photo of a traveller in front of a red suspension bridge" style="background:linear-gradient(180deg,#7fa6cf,#b0503a 55%,#5a5a52)"></div>
      <div class="post-body">
        <h3 class="post-title">THE BEST TRAVEL IN YEARS</h3>
        <p class="post-author">by <span>Dara Wendt</span></p>
        <p class="post-text">Lorem ipsum dolor sit amet, consectetur adipisicing elit, sed do eiusmod tempor incididunt ut labore et dolore magna aliqua. Ut enim ad minim veniam, quis nostrud exercitation ullamco laboris nisi ut aliquip ex ea commodo consequat. Duis aute irure dolor in reprehenderit in voluptate velit esse cillum dolore eu fugiat nulla pariatur. Excepteur sint occaecat....</p>
      </div>
      <span class="read-more">READ POST ›</span>
    </article>

    <div class="forum-btn">VISIT FORUMS</div>
  </section>

  <footer class="footer">
    <div class="f-col" style="left:216px"><h4>SITE MAP</h4><a>Flights</a><a>Hotels</a><a>Cars</a><a>Solutions</a></div>
    <div class="f-col" style="left:413px"><h4>RESOURCES</h4><a>Hotel Insurance</a><a>Extra Costs</a><a>Resort Locations</a><a>Cheap Flights</a></div>
    <div class="f-col" style="left:667px"><h4>COMPANY</h4><a>About</a><a>Forums</a><a>Success Stories</a><a>Contact</a></div>
    <div class="f-col" style="left:872px"><h4>SUPPORT</h4><a>Support Center</a><a>Community</a></div>
    <p class="copyright">© Mirdalon, Inc. <span>Terms</span> <span>Privacy Policy</span></p>
    <div class="social"><i></i><i></i><i></i><i></i><i></i></div>
  </footer>
</div>
</body>
</html>
```